Counseling Practice Business Card

I need a professional looking business card incorporating my new logo that was just completed. Card needs to incorporate my name and title, description of my specialty, my address, my phone number, my fax number, my email and my website URL. I need to be able to choose design on/with different paper colors and textures.
I do not have a lot of business card ideas so I am open to anything but I want bold,sharp, clear card without additional designs other than my logo (see attached file info). I am open to different color backgrounds or paper colors including black. I do not like traditional brackets around area codes in phone number or dashes between numbers in phone number. Am open to other ways of presenting including periods between numbers as appropriate. I do not know enough to know what I like yet but I want card to coordinate and work together with my logo. My practice emphasizes natural mental health interventions so any use of color (with background paper color or the blue and green in my logo) that elicits nature is nice. In addition to black, any natural brown or wood looking background might be desirable also. Most of the offerings so far look very similar and boring.

Target Market(s)

Potential therapy clients and other professionals

Contact Information for Business Card

Card information:
Marcus T. Whitfield, Ph.D.
Licensed Clinical Psychologist
Integrative Health Coach
4812 Ferndale Pkwy NW
Suite 730
Ashbury, GA 30418
555 555 0142 phone
555 555 0186 fax
drmarcuswhitfield@kelvora.com
pathbloomcounseling.com

Font styles to use
Serif
Sans Serif
Other font styles liked:
• anything that you think looks crisp, clear and easily readable

Requirements
Must have
• Any color used should coordinate with my logo design (see attached files).
• Card should be printed horizontally so top and bottom are longest sides of rectangle.
• Background color or paper color should complement and highlight logo. Do not like a white background. black, grey, brown or any color my logo would blend well with.
Nice to have
• I would like designer to utilize color to highlight letters/name or phone-fax-web symbols.
• Bottom edge of card could be highlighted if appropriate to an idea.
Should not have
• I would NOT want the card to have a pure white background at all.
• No clear cards.
• Cards should be oriented with long sides on bottom and top, NOT sides. DO NOT LIKE THIS THIN TALL ORIENTATION.

```html
<!DOCTYPE html>
<html lang="en">
<head>
<meta charset="utf-8">
<title>Pathbloom Counseling – Business Card</title>
<link rel="stylesheet" href="https://fonts.googleapis.com/css2?family=Arimo:wght@400;700&display=swap">
<style>
  :root {
    --kraft: #a38f74;
    --kraft-dark: #8f7b61;
    --ink: #111111;
    --leaf-green: #1f8c22;
    --sky-blue: #3b8fe6;
    --backdrop: #000000;
  }
  * { margin: 0; padding: 0; box-sizing: border-box; }
  html, body {
    width: 1200px;
    height: 777px;
    overflow: hidden;
    background: var(--backdrop);
  }
  .card {
    position: relative;
    width: 1200px;
    height: 777px;
    background: linear-gradient(160deg, var(--kraft) 0%, var(--kraft-dark) 100%);
    border-radius: 0 0 26px 26px;
    font-family: "Arimo", Arial, sans-serif;
    color: var(--ink);
    overflow: hidden;
  }
  .brand {
    position: absolute;
    left: 64px;
    top: 98px;
    color: var(--leaf-green);
    font-weight: 700;
    line-height: 1;
  }
  .brand-mark {
    display: inline-block;
    width: 34px;
    height: 34px;
    border-radius: 50%;
    background: var(--sky-blue);
    vertical-align: middle;
    margin-right: 18px;
    position: relative;
    top: -10px;
  }
  .brand-name {
    font-size: 104px;
    letter-spacing: -2px;
  }
  .brand-sub {
    display: block;
    font-size: 34px;
    letter-spacing: 17px;
    text-transform: uppercase;
    margin: 18px 0 0 56px;
  }
  .branch-art {
    position: absolute;
    left: 680px;
    top: 0;
    width: 520px;
    height: 585px;
    background: radial-gradient(ellipse at 55% 40%, rgba(31,140,34,0.28) 0%, rgba(31,140,34,0.12) 45%, rgba(31,140,34,0) 72%);
  }
  .contact {
    position: absolute;
    left: 58px;
    top: 424px;
    font-size: 31px;
    line-height: 1.0;
  }
  .address p { margin-bottom: 13px; }
  .lines { margin-top: 26px; }
  .lines p { margin-bottom: 13px; }
  .lines strong { font-weight: 700; }
  .email { margin-top: 30px; }
  .website {
    margin-top: 12px;
    font-size: 39px;
    font-weight: 700;
  }
  .person {
    position: absolute;
    right: 30px;
    top: 604px;
    text-align: right;
  }
  .person-name {
    font-size: 47px;
    font-weight: 700;
    line-height: 1;
  }
  .person-name small {
    font-size: 26px;
    font-weight: 700;
  }
  .person-title {
    font-size: 33px;
    line-height: 1;
    margin-top: 14px;
  }
  .person-title + .person-title { margin-top: 13px; }
</style>
</head>
<body>
  <div class="card">
    <div class="brand">
      <span class="brand-mark"></span><span class="brand-name">Pathbloom</span>
      <span class="brand-sub">Counseling</span>
    </div>

    <div class="branch-art" role="img" aria-label="Green line-drawn leafy branch reaching in from the top right corner"></div>

    <div class="contact">
      <div class="address">
        <p>4812 Ferndale Pkwy NW</p>
        <p>Suite 730, Ashbury, GA 30418</p>
      </div>
      <div class="lines">
        <p><strong>555</strong> 555 0142 <strong>phone</strong></p>
        <p><strong>555</strong> 555 0186 <strong>fax</strong></p>
      </div>
      <p class="email">drmarcuswhitfield@kelvora.com</p>
      <p class="website">pathbloomcounseling.com</p>
    </div>

    <div class="person">
      <p class="person-name">Marcus T. Whitfield <small>Ph.D.</small></p>
      <p class="person-title">Licensed Clinical Psychologist</p>
      <p class="person-title">Integrative Health Coach</p>
    </div>
  </div>
</body>
</html>
```